Design Concept for various leaflets and banners etc

Create a print design concept that can be utilized across multiple formats eg leaflets, booklets, banners, website.We currently have an collection of print materials with various design styles. We wish to create a look which makes these items more cohesive as a group.The creative should sit comfortably with existing A5 landscape brochure artwork and exhibition banners. The design concept provided should have no inherent meaning in itself. Preferred colours are blue and green. The colours used should be in-keeping with the colour guide attached. This look will mainly be employed on A6 flyers, DL Flyers, business cards and signage.The look should be simple yet modern and serious. The look should allow maximum flexibility in deployment. (Epically considering we have over 30 different leaflets that need to be visibly different but yet seen as a family of leaflets.) Our main website address is also our ‘brand’ ie www.Rune-vo.net . We also have a sister project called the Harrow Exhibition.

Target Market(s)

Public

Industry/Entity Type

Christian

Requirements
Must have
• Flexibility in application.
Should not have
• No inherent meaning

```html
<!DOCTYPE html>
<html lang="en">
<head>
<meta charset="utf-8">
<title>Leaflet Family – Cover Concepts</title>
<link rel="stylesheet" href="https://fonts.googleapis.com/css2?family=Raleway:wght@300;400;800&display=swap">
<style>
  :root {
    --navy: #1e3768;
    --navy-deep: #182a55;
    --ink: #15234a;
    --silver-light: #f4f5f6;
    --silver-mid: #d9dadc;
    --silver-dark: #c4c6c9;
    --teal: #2fbf9c;
    --blue: #1b86c4;
    --white: #ffffff;
    --sand: #c9b48a;
    --wood: #8a5a34;
  }
  html, body {
    margin: 0;
    padding: 0;
    width: 1200px;
    height: 1200px;
    overflow: hidden;
    background: var(--white);
  }
  .canvas {
    position: relative;
    width: 1200px;
    height: 1200px;
    background: var(--white);
  }
  .leaflet {
    position: absolute;
    top: 220px;
    width: 540px;
    height: 760px;
    overflow: hidden;
    font-family: 'Raleway', sans-serif;
  }
  .leaflet--wrong { left: 40px; }
  .leaflet--eternity { left: 620px; }
  .leaflet__art {
    position: absolute;
    inset: 0;
    width: 540px;
    height: 760px;
  }
  .leaflet__headline {
    position: absolute;
    margin: 0;
    color: var(--ink);
    font-weight: 800;
    font-size: 60px;
    line-height: 1.08;
    letter-spacing: 0.5px;
    text-align: center;
  }
  .leaflet--wrong .leaflet__headline {
    top: 150px;
    left: 60px;
    width: 440px;
  }
  .leaflet--eternity .leaflet__headline {
    top: 130px;
    left: 60px;
    width: 440px;
  }
  .brand-mark {
    position: absolute;
    right: 60px;
    bottom: 60px;
    color: var(--white);
    font-weight: 400;
    font-size: 40px;
    letter-spacing: 0.5px;
  }
  .hourglass-visual {
    position: absolute;
    left: 70px;
    top: 430px;
    width: 170px;
    height: 290px;
    border-radius: 14px;
    background: linear-gradient(180deg, var(--wood) 0%, var(--sand) 45%, var(--sand) 60%, var(--wood) 100%);
  }
  .verse {
    position: absolute;
    right: 36px;
    bottom: 70px;
    width: 230px;
    margin: 0;
    color: var(--white);
    font-weight: 300;
    font-size: 14px;
    line-height: 1.4;
    text-align: right;
  }
  .verse__ref {
    display: block;
    margin-top: 14px;
    font-size: 12px;
  }
</style>
</head>
<body>
<div class="canvas">

  <section class="leaflet leaflet--wrong">
    <svg class="leaflet__art" viewBox="0 0 540 760" aria-hidden="true">
      <defs>
        <linearGradient id="silverA" x1="0" y1="0" x2="1" y2="1">
          <stop offset="0" stop-color="var(--silver-dark)"/>
          <stop offset="0.5" stop-color="var(--silver-light)"/>
          <stop offset="1" stop-color="var(--silver-mid)"/>
        </linearGradient>
        <linearGradient id="accentA" x1="0" y1="0" x2="1" y2="0">
          <stop offset="0" stop-color="var(--teal)"/>
          <stop offset="0.5" stop-color="var(--blue)"/>
          <stop offset="1" stop-color="var(--teal)"/>
        </linearGradient>
        <linearGradient id="navyA" x1="0" y1="0" x2="0" y2="1">
          <stop offset="0" stop-color="var(--navy-deep)"/>
          <stop offset="1" stop-color="var(--navy)"/>
        </linearGradient>
      </defs>
      <rect class="band-navy" width="540" height="760" fill="url(#navyA)"/>
      <path class="band-white" fill="var(--white)" d="M0,210 Q30,40 230,0 L540,0 L540,400 Q420,620 0,650 Z"/>
      <path class="band-accent" fill="url(#accentA)" d="M0,232 Q46,50 258,0 L540,0 L540,386 Q420,606 0,632 Z"/>
      <path class="band-silver" fill="url(#silverA)" d="M0,250 Q60,60 280,0 L540,0 L540,370 Q420,590 0,615 Z"/>
    </svg>
    <h1 class="leaflet__headline">What if you are wrong about God?</h1>
    <div class="brand-mark">Rune-vo</div>
  </section>

  <section class="leaflet leaflet--eternity">
    <svg class="leaflet__art" viewBox="0 0 540 760" aria-hidden="true">
      <defs>
        <linearGradient id="silverB" x1="0" y1="0" x2="1" y2="1">
          <stop offset="0" stop-color="var(--silver-dark)"/>
          <stop offset="0.5" stop-color="var(--silver-light)"/>
          <stop offset="1" stop-color="var(--silver-mid)"/>
        </linearGradient>
        <linearGradient id="accentB" x1="0" y1="0" x2="1" y2="0">
          <stop offset="0" stop-color="var(--teal)"/>
          <stop offset="0.5" stop-color="var(--blue)"/>
          <stop offset="1" stop-color="var(--teal)"/>
        </linearGradient>
        <linearGradient id="navyB" x1="0" y1="0" x2="0" y2="1">
          <stop offset="0" stop-color="var(--navy-deep)"/>
          <stop offset="1" stop-color="var(--navy)"/>
        </linearGradient>
      </defs>
      <rect class="band-navy" width="540" height="760" fill="url(#navyB)"/>
      <path class="band-white" fill="var(--white)" d="M0,210 Q30,40 230,0 L540,0 L540,400 Q420,620 0,650 Z"/>
      <path class="band-accent" fill="url(#accentB)" d="M0,232 Q46,50 258,0 L540,0 L540,386 Q420,606 0,632 Z"/>
      <path class="band-silver" fill="url(#silverB)" d="M0,250 Q60,60 280,0 L540,0 L540,370 Q420,590 0,615 Z"/>
    </svg>
    <h1 class="leaflet__headline">Where will you spend Eternity?</h1>
    <div class="hourglass-visual" role="img" aria-label="Wooden hourglass with sand running through it"></div>
    <p class="verse">“For the wages of sin is death; but the gift of God is eternal life through Jesus Christ our Lord.”<span class="verse__ref">Romans 6:23</span></p>
  </section>

</div>
</body>
</html>
```